Business Card Design

We need a business card designed which uses our logo and looks really good. The company is called Veltramor482. We help e-commerce companies reduce cart abandonment by rescuing the sale through our innovative technology.

Our corporate colors are red, black and white.

I have attached our AI file for the logo as well.

Additional information for the business card:

Name: Marcus Delby
Title: President/CTO
Phone: 1-877-VELT-482
Website: www.veltramor482.com
Email: marcus@veltramor482.com

Tag line: Keeping Every Sale In Reach

Industry/Entity Type

E-Commerce

```html
<!DOCTYPE html>
<html lang="en">
<head>
<meta charset="utf-8">
<title>Veltramor482 Business Card</title>
<link rel="stylesheet" href="https://fonts.googleapis.com/css2?family=Arimo:wght@400;700&display=swap">
<style>
  :root {
    --page: #ffffff;
    --card-white: #ffffff;
    --band-light: #ececec;
    --panel-grey: #686868;
    --brand-red: #e41e26;
    --brand-black: #141414;
    --text-white: #ffffff;
  }
  * { margin: 0; padding: 0; box-sizing: border-box; }
  html, body {
    width: 1200px; height: 1000px; overflow: hidden;
    background: var(--page);
    font-family: "Arimo", Arial, sans-serif;
  }
  .business-card {
    position: absolute; left: 98px; top: 218px;
    width: 1000px; height: 568px;
    background: var(--card-white);
  }
  .brand-area {
    position: absolute; left: 0; top: 0; width: 100%; height: 199px;
    display: flex; align-items: center; justify-content: center; gap: 26px;
    padding-top: 12px;
  }
  .brand-mark {
    width: 62px; height: 62px; background: var(--brand-red);
  }
  .brand-name {
    font-size: 96px; font-weight: 400; color: var(--brand-black);
    letter-spacing: 3px; line-height: 1;
  }
  .tagline-band {
    position: absolute; left: 0; top: 199px; width: 100%; height: 50px;
    background: var(--band-light);
    display: flex; align-items: center; justify-content: center;
  }
  .tagline {
    color: var(--brand-red); font-size: 30px; font-weight: 400; letter-spacing: 3.5px;
    word-spacing: 10px; text-transform: uppercase; line-height: 1;
  }
  .contact-panel {
    position: absolute; left: 0; top: 249px; width: 100%; height: 319px;
    background: var(--panel-grey); color: var(--text-white);
  }
  .person-name {
    position: absolute; left: 42px; top: 100px;
    font-size: 57px; font-weight: 400; letter-spacing: 3px; line-height: 1;
  }
  .person-title {
    position: absolute; left: 42px; top: 193px;
    font-size: 54px; font-weight: 400; letter-spacing: 3px; line-height: 1;
  }
  .contact-list { position: absolute; left: 556px; top: 90px; list-style: none; }
  .contact-item {
    display: flex; align-items: center; height: 32px; margin-bottom: 33px;
    font-size: 22px; letter-spacing: 2px;
  }
  .contact-item:nth-child(2) { margin-bottom: 34px; }
  .contact-icon { width: 36px; height: 32px; margin-right: 30px; fill: var(--text-white); }
</style>
</head>
<body>
  <div class="business-card">
    <header class="brand-area">
      <span class="brand-mark"></span>
      <span class="brand-name">Veltramor482</span>
    </header>
    <div class="tagline-band">
      <p class="tagline">Keeping Every Sale In Reach</p>
    </div>
    <section class="contact-panel">
      <h1 class="person-name">Marcus Delby</h1>
      <p class="person-title">President/CTO</p>
      <ul class="contact-list">
        <li class="contact-item">
          <svg class="contact-icon" viewBox="0 0 36 32" aria-hidden="true">
            <path d="M8 22 C4 18 4 13 7 11 L11 16 C10 18 11 19 13 21 C15 23 16 24 18 23 L23 27 C21 30 16 30 12 26 Z"/>
            <path d="M13 9 L17 5 L22 11 L18 14 Z M24 21 L28 17 L34 22 L30 26 Z"/>
          </svg>
          <span>1-877-VELT-482</span>
        </li>
        <li class="contact-item">
          <svg class="contact-icon" viewBox="0 0 36 32" aria-hidden="true">
            <circle cx="18" cy="16" r="15"/>
            <path d="M10 9 C13 7 16 8 16 11 C15 13 13 13 13 16 C13 19 11 20 10 18 C8 15 8 12 10 9 Z M20 17 C23 16 26 18 25 22 C24 26 21 26 21 23 C20 21 19 19 20 17 Z M22 6 C25 7 27 9 26 11 C24 11 22 9 22 6 Z" fill="#686868"/>
          </svg>
          <span>www.veltramor482.com</span>
        </li>
        <li class="contact-item">
          <svg class="contact-icon" viewBox="0 0 36 32" aria-hidden="true">
            <path d="M0 4 H36 V28 H0 Z"/>
            <path d="M1 5 L18 19 L35 5 M1 27 L13 15 M35 27 L23 15" fill="none" stroke="#686868" stroke-width="2"/>
          </svg>
          <span>marcus@veltramor482.com</span>
        </li>
      </ul>
    </section>
  </div>
</body>
</html>
```